Banner 170x60 for Barrel Sauna Rental Banner

Attention, please do every side graphic distance 5cm . It is for attachment.
search for a graphic design in dimension 170x60cm.
we have a barrel sauna rental service and need a banner for the two sides.
please look photos.
big text is: (SAUNA FOR RENT!! )in english like: you can rent me
frohe-kistenwelt.de
015293417720
info@frohe-kistenwelt.de
we need an eye catcher design!!!!
Design:
maybe wood in at background.
maybe burning fire and sauna style.
Please don't use my barrell sauna pictures. It is only an example for you what we do. The barrel sauna is on build at the moment.

```html
<!DOCTYPE html>
<html lang="en">
<head>
<meta charset="utf-8">
<title>Sauna For Rent – Rental Banner</title>
<link rel="stylesheet" href="https://fonts.googleapis.com/css2?family=Roboto+Condensed:wght@700&family=Roboto:wght@500;700;900&display=swap">
<style>
  :root {
    --stage-dark: #1b1a1a;
    --stage-light: #ffffff;
    --wood-deep: #1e130d;
    --wood-mid: #4a2814;
    --ember: #a4511c;
    --glow: #d27a2e;
    --text-white: #ffffff;
    --text-yellow: #f7c600;
    --frame-line: #bdb7b2;
  }
  * { margin: 0; padding: 0; box-sizing: border-box; }
  html, body { width: 1200px; height: 1200px; overflow: hidden; }
  body { position: relative; background: var(--stage-light); }
  .stage-dark {
    position: absolute; left: 0; top: 0; width: 1200px; height: 557px;
    background: var(--stage-dark);
  }
  .banner {
    position: absolute;
    width: 412px; height: 147px;
    overflow: hidden;
    text-align: center;
  }
  .banner--on-dark { left: 387px; top: 199px; border: 2px solid var(--frame-line); }
  .banner--on-light { left: 384px; top: 785px; }
  .banner__backdrop {
    position: absolute; inset: 0;
    background:
      radial-gradient(ellipse 45% 60% at 50% 45%, var(--glow) 0%, var(--ember) 30%, rgba(74,40,20,0) 75%),
      linear-gradient(90deg, var(--wood-deep) 0%, var(--wood-mid) 35%, var(--wood-mid) 65%, var(--wood-deep) 100%);
  }
  .banner__line {
    position: absolute; left: 0; right: 0;
    transform: translateY(-50%);
    white-space: nowrap; line-height: 1;
    text-shadow: 0 1px 3px rgba(0,0,0,0.6);
  }
  .banner__headline {
    top: 18%;
    font-family: "Roboto Condensed", "Arial Narrow", sans-serif;
    font-weight: 700; font-size: 44px; color: var(--text-white);
  }
  .banner__phone {
    top: 45%;
    font-family: "Roboto", Arial, sans-serif;
    font-weight: 900; font-size: 37px; color: var(--text-yellow);
  }
  .banner__web {
    top: 70%;
    font-family: "Roboto", Arial, sans-serif;
    font-weight: 500; font-size: 24px; color: var(--text-white);
  }
  .banner__mail {
    top: 88%;
    font-family: "Roboto", Arial, sans-serif;
    font-weight: 500; font-size: 20px; color: var(--text-white);
    letter-spacing: 2.5px;
  }
</style>
</head>
<body>
  <div class="stage-dark"></div>

  <div class="banner banner--on-dark">
    <div class="banner__backdrop" role="img" aria-label="Wood and fire background in warm brown and orange tones"></div>
    <p class="banner__line banner__headline">SAUNA FOR RENT!!</p>
    <p class="banner__line banner__phone">015293417720</p>
    <p class="banner__line banner__web">frohe-kistenwelt.de</p>
    <p class="banner__line banner__mail">info@frohe-kistenwelt.de</p>
  </div>

  <div class="banner banner--on-light">
    <div class="banner__backdrop" role="img" aria-label="Wood and fire background in warm brown and orange tones"></div>
    <p class="banner__line banner__headline">SAUNA FOR RENT!!</p>
    <p class="banner__line banner__phone">015293417720</p>
    <p class="banner__line banner__web">frohe-kistenwelt.de</p>
    <p class="banner__line banner__mail">info@frohe-kistenwelt.de</p>
  </div>
</body>
</html>
```